Pelmora needs stationery design

We need desings for presentation cards and letter head for our company. It would be better that the letterhead uses our logo with white background and the presentation card the logo with the black background for the back of the card and the text (name, phone
Updates

Necesitas un par de días antes de escoger al ganador

Colors
0455a3
ec1f27
000000

Requirements
Must have
• Use company logo and colors

```html
<!DOCTYPE html>
<html lang="en">
<head>
<meta charset="utf-8">
<title>Pelmora business card</title>
<link href="https://fonts.googleapis.com/css2?family=Lato:wght@400;700&display=swap" rel="stylesheet">
<style>
  :root {
    --blue: #0455a3;
    --red: #ec1f27;
    --black: #050606;
    --ink: #1b1b1b;
    --grey-text: #555;
    --card-light: #eeeeee;
    --rule: #a8a8a8;
    --backdrop: #d3d3d3;
  }
  * { margin: 0; padding: 0; box-sizing: border-box; }
  html, body { width: 1200px; height: 1134px; overflow: hidden; }
  body {
    background: var(--backdrop);
    font-family: "Lato", sans-serif;
    position: relative;
  }
  .card {
    position: absolute;
    left: 266px;
    width: 653px;
    height: 373px;
  }
  .card-front { top: 164px; background: var(--card-light); }
  .card-back { top: 602px; background: var(--black); }

  .wordmark {
    position: absolute;
    font-family: "Lato", sans-serif;
    font-weight: 400;
    text-transform: uppercase;
    line-height: 1;
  }
  .card-front .wordmark {
    left: 39px; top: 58px;
    font-size: 48px; letter-spacing: 2px;
    color: var(--ink);
  }
  .card-back .wordmark {
    left: 0; right: 0; top: 174px;
    text-align: center;
    font-size: 64px; letter-spacing: 3px;
    color: #ffffff;
  }

  .holder-name {
    position: absolute; left: 39px; top: 150px;
    font-size: 25px; font-weight: 700; color: var(--blue);
  }
  .holder-role {
    position: absolute; left: 39px; top: 179px;
    font-size: 17px; color: var(--grey-text);
  }
  .divider {
    position: absolute; left: 39px; top: 208px;
    width: 569px; height: 2px; background: var(--rule);
  }
  .contact-list {
    position: absolute; left: 39px; top: 222px;
    list-style: none;
  }
  .contact-list li {
    display: flex; align-items: center; gap: 7px;
    height: 22px; font-size: 15.5px; color: var(--grey-text);
  }
  .contact-list svg { width: 14px; height: 14px; fill: var(--red); flex: none; }
  .website {
    position: absolute; right: 45px; top: 276px;
    font-size: 15.5px; color: var(--grey-text);
  }
  .website .accent { color: var(--red); }

  .address-bar {
    position: absolute; left: 0; top: 316px;
    width: 100%; height: 34px; background: var(--black);
  }
  .address-bar .address {
    position: absolute; left: 42px; top: 7px;
    font-size: 15.5px; color: #ffffff;
  }
  .address-bar .mark-gap {
    position: absolute; left: 508px; top: 0;
    width: 36px; height: 34px; background: var(--card-light);
  }
  .address-bar .mark-square {
    position: absolute; left: 6px; top: 5px;
    width: 24px; height: 24px; background: var(--blue);
  }
</style>
</head>
<body>
  <section class="card card-front">
    <div class="wordmark">Pelmora</div>
    <div class="holder-name">Dorian Vell</div>
    <div class="holder-role">President</div>
    <div class="divider"></div>
    <ul class="contact-list">
      <li>
        <svg viewBox="0 0 16 16" aria-hidden="true"><path d="M3.6 1.2l2.3 2.6-1.3 1.8c.9 2 2.5 3.6 4.5 4.6l1.8-1.4 2.7 2.3-1.4 2.6C7 13.5 2.3 8.8 2 2.5z"/></svg>
        555 210 4477
      </li>
      <li>
        <svg viewBox="0 0 16 16" aria-hidden="true"><path d="M4.5 0.5h7a1 1 0 0 1 1 1v13a1 1 0 0 1-1 1h-7a1 1 0 0 1-1-1v-13a1 1 0 0 1 1-1zm0.8 2v10h5.4v-10z"/></svg>
        555 389 1602
      </li>
      <li>
        <svg viewBox="0 0 16 16" aria-hidden="true"><path d="M1 3h14v1.2L8 8.6 1 4.2z M1 5.8l7 4.4 7-4.4V13H1z"/></svg>
        hello@pelmora.co
      </li>
    </ul>
    <div class="website">www.<span class="accent">pelmora</span>.co</div>
    <div class="address-bar">
      <span class="address">Level 5, 27 Harlow Lane, Eastbrook, VIC 3100</span>
      <div class="mark-gap"><div class="mark-square"></div></div>
    </div>
  </section>

  <section class="card card-back">
    <div class="wordmark">Pelmora</div>
  </section>
</body>
</html>
```